New high end server provider needs wordpress design

www.kv7hosting.com

Need a wordpress design for a high end server provider that provides overclocked dedicated servers for rent. We are located in Chicago but we have a presence is Virginia and Nevada for both our east and west coast customers.

We are a server provider that specializes in top end hardware with every feature designed for optimum performance. If it is not the best quality part or provides the best possible performance we don't run it. Our customers are mainly those that want the best single threaded performance possible from their hardware. We would be selling our services directly on our website via WHMCS.

We would like to see designs that are very modern and simplistic yet very attractive looking and catchy. Would prefer colors in the blues and greens and white. These colors are not necessary and I would be open to another color scheme if it looks good.

The final design should show speed and performance while being simplistic and easy on the eyes.

Logo and company name added and payment changed to guaranteed.  Looking for a wordpress template with the same pages as kv7hosting.com but with a redesigned look and feel.  

WHMCS control panel design also part of the design request.

If you have any questions please let me know!  This is just for kv7hosting.com and a main page for WHMCS (no coding just design).

Target Market(s)

IT Guru's (mostly men in their 20's to 30's)

Industry/Entity Type

Hardware

Requirements
Must have
• WHMCS panel design to fit with website theme.
Nice to have
• Main slider on home page similar to one of our other websites at www.kv7hosting.com
Should not have
• Flash or frames

```html
<!DOCTYPE html>
<html lang="en">
<head>
<meta charset="utf-8">
<title>KV7Hosting – Home</title>
<link href="https://fonts.googleapis.com/css2?family=Cabin:wght@400;500;600;700&family=Open+Sans:wght@400;600;700&display=swap" rel="stylesheet">
<style>
:root{
  --ink:#2b2b2b;
  --body:#3a3a3a;
  --header-dark:#243238;
  --header-mid:#33454c;
  --accent-green:#9bd21c;
  --nav-top:#8fd6ef;
  --nav-bot:#3aaad6;
  --nav-active:#174f66;
  --link:#1f9bd2;
  --teal-title:#1c7fa8;
  --panel-dark:#2f4a55;
  --panel-grey:#3b3f42;
  --tweet-head:#8fb0bd;
  --tweet-bg:#e3f3f9;
  --footer:#262626;
  --footer-link:#9a9a9a;
  --footer-head:#6fa3b8;
  --sky:#d3ecf5;
}
*{box-sizing:border-box;margin:0;padding:0}
html,body{width:917px;height:1200px;overflow:hidden}
body{position:relative;font-family:"Cabin",sans-serif;color:var(--body);
  background:linear-gradient(#cfe9f3 0,#eef7fa 260px,#f6f9fa 600px,#eef1f2 1060px)}
.abs{position:absolute}
.topbar{left:0;top:0;width:917px;height:48px;background:linear-gradient(var(--header-mid),var(--header-dark))}
.brand{left:100px;top:11px;display:flex;align-items:center;gap:8px;font-family:"Cabin",sans-serif;font-weight:700;font-size:22px;color:#dbe6ea;letter-spacing:.5px}
.brand-dot{width:24px;height:24px;border-radius:50%;background:#5fa9c4}
.session{right:106px;top:16px;font-size:11px;color:#fff}
.session em{font-style:normal;color:var(--accent-green)}
.sheet{left:95px;top:48px;width:727px;height:1019px;background:linear-gradient(#fff 0,#fff 500px,#f7f9fa 1019px)}
.nav{left:87px;top:60px;width:743px;height:32px;background:linear-gradient(var(--nav-top),var(--nav-bot));display:flex;align-items:center;padding-left:15px;gap:0}
.nav a{font-size:13px;color:#fff;text-decoration:none;padding:6px 12px;font-family:"Cabin",sans-serif}
.nav a.active{background:var(--nav-active);border:1px solid #0d3444}
.nav-fold{top:92px;width:0;height:0;border-top:12px solid #1d6f90}
.fold-l{left:87px;border-left:8px solid transparent}
.fold-r{left:822px;border-right:8px solid transparent}
.slider{left:102px;top:104px;width:711px;height:261px;background:linear-gradient(120deg,#6b6b5e 0,#3c4658 30%,#8a8c8a 55%,#2d2d2d 75%,#8a4a2a 100%);box-shadow:0 8px 12px -6px rgba(0,0,0,.35)}
.slide-title{left:122px;top:166px;font-family:"Open Sans",sans-serif;font-weight:700;font-size:31px;color:#fff;line-height:40px}
.slide-title span{display:inline-block;background:rgba(20,20,20,.75);padding:0 10px}
.slide-copy{left:122px;top:260px;width:356px;background:rgba(20,20,20,.75);padding:4px 10px;font-size:11px;color:#6fd0f5;line-height:19px}
.slide-copy b{color:#fff;font-size:14px}
.dots{left:743px;top:338px;display:flex;gap:6px}
.dots i{width:14px;height:14px;border-radius:50%;background:#fff}
.dots i:first-child{background:#1c7fa8}
.domain-title{left:0;width:917px;top:411px;text-align:center;font-size:17px;font-weight:700;color:var(--teal-title)}
.domain-lead{left:0;width:917px;top:439px;text-align:center;font-size:10px;color:#444}
.domain-input{left:231px;top:462px;width:453px;height:35px;border:1px solid #bfbfbf;background:#ececec;padding:10px 7px;font-size:13px;color:#888}
.btn{top:509px;height:26px;border-radius:3px;font-size:11px;color:#fff;display:flex;align-items:center;justify-content:center}
.btn-check{left:308px;width:106px;background:linear-gradient(#6fd2f8,#2ea6d9);border:1px solid #1d83b0}
.btn-transfer{left:420px;width:64px;background:linear-gradient(#a9dc2a,#6ea50c);border:1px solid #5b8a0a}
.btn-hosting{left:490px;width:119px;background:linear-gradient(#9a9a9a,#6a6a6a);border:1px solid #555}
.divider{left:150px;top:557px;width:600px;height:2px;background:radial-gradient(ellipse at center,#cfcfcf 0,transparent 70%)}
h2{font-family:"Cabin",sans-serif;font-weight:600;font-size:17px;color:var(--ink)}
.welcome{left:108px;top:594px;width:425px}
.welcome p{font-size:9.6px;line-height:12.6px;margin-top:13px;color:#3a3a3a}
.welcome p:first-of-type{margin-top:6px}
.welcome a{color:var(--link);text-decoration:none}
.offer{left:108px;top:837px;width:430px}
.offer ul{list-style:none;margin-top:13px}
.offer li{font-size:10px;display:flex;align-items:center;gap:7px;height:25.5px}
.offer li i{width:12px;height:12px;border-radius:50%;background:#8ccbe6;position:relative}
.offer li i::before,.offer li i::after{content:"";position:absolute;background:#fff;left:5px;top:2px;width:2px;height:8px}
.offer li i::after{left:2px;top:5px;width:8px;height:2px}
.cta{left:565px;width:243px;height:42px;padding:6px 15px;color:#fff;clip-path:polygon(0 0,92% 0,100% 50%,92% 100%,0 100%)}
.cta strong{display:block;font-size:16px;font-weight:600}
.cta small{font-size:9.5px;color:#cfe0e6}
.cta-order{top:597px;background:var(--panel-dark)}
.cta-account{top:651px;background:var(--panel-grey)}
.tweets{left:565px;top:705px;width:244px;height:348px;background:var(--tweet-bg)}
.tweets-head{height:28px;background:var(--tweet-head);color:#fff;font-size:16px;font-weight:600;padding:4px 16px}
.tweet-list{list-style:none;margin:0 0 0 16px;width:209px}
.tweet-list li{position:relative;font-size:9.6px;line-height:12.5px;color:#333;padding:9px 36px 8px 0;border-bottom:1px dashed #b9cdd4}
.tweet-list li span{color:var(--link)}
.tweet-list li i{position:absolute;right:4px;top:12px;width:22px;height:16px;border-radius:50%;background:#b8c6cc}
.footer{left:0;top:1067px;width:917px;height:133px;background:var(--footer)}
.fcol{top:1081px;font-size:8px}
.fcol h4{font-size:10px;font-weight:400;color:var(--footer-head);margin-bottom:8px}
.fcol a{display:block;color:var(--footer-link);text-decoration:underline;line-height:13.5px}
.badges{left:583px;top:1082px;display:flex;gap:10px}
.badges i{height:22px;background:#4a4a4a;border-radius:3px}
.social{left:735px;top:1124px;font-size:8px;color:#aaa;display:flex;align-items:center;gap:4px}
.social i{width:12px;height:12px;background:#8fbcd4;border-radius:2px}
.footer-rule{left:95px;top:1151px;width:727px;height:1px;background:#3a3a3a}
.copyright{left:0;width:917px;top:1161px;text-align:center;font-size:8px;color:#aaa}
</style>
</head>
<body>
<header class="abs topbar"></header>
<div class="abs brand"><span class="brand-dot"></span>KV7HOSTING</div>
<div class="abs session">Logged in as <em>Administrator</em> | Return to <em>Admin</em> Area</div>

<div class="abs sheet"></div>
<nav class="abs nav">
  <a class="active">Home</a><a>Our Servers</a><a>Dedicated Servers</a><a>Why KV7?</a><a>Testimonials</a><a>FAQ's</a><a>Contacts</a>
</nav>
<div class="abs nav-fold fold-l"></div>
<div class="abs nav-fold fold-r"></div>

<section class="abs slider" role="img" aria-label="Close-up photo of server hardware with CPU cooler and heatsink"></section>
<div class="abs slide-title"><span>Overclocked</span><br><span>High Quality Hardware</span></div>
<p class="abs slide-copy">Our hardware is top of the line featuring overclocked <b>Nova Core X5 2500k</b> Processors running at 4.5 Ghz</p>
<div class="abs dots"><i></i><i></i><i></i></div>

<h3 class="abs domain-title">Choose a Domain...</h3>
<p class="abs domain-lead">Start your web hosting experience with us by entering the domain name you want to register, transfer or simply purchase hosting for below...</p>
<div class="abs domain-input">e.g yourdomain.com</div>
<div class="abs btn btn-check">Check Availability</div>
<div class="abs btn btn-transfer">Transfer</div>
<div class="abs btn btn-hosting">Order Hosting Only</div>
<div class="abs divider"></div>

<article class="abs welcome">
  <h2>Welcome</h2>
  <p>KV7Hosting offer the highest quality, highest performing Siege Protocol 2 servers available for rent. Our servers are custom built specifically for the demanding requirements of Siege Protocol 2 Beta. Each Siege Protocol 2 game server is ran on a 4.4 Ghz overclocked Nova Core X5 2500k CPU, so you can be assured that our servers will be able to run at high tickrates with 20+ players.</p>
  <p>Unlike most game server providers, we offer unlimited player slots on all of our rentals. This means that you can increase the player count when the game becomes more optimized, ensuring that your server will always be one of the most popular and best performing Siege Protocol 2 servers around.</p>
  <p>Interested in ordering? See our Pricing Page for more information.</p>
  <p>Have any questions? We have multiple contact methods located on our <a>Contacts</a> Page</p>
</article>

<section class="abs offer">
  <h2>What we offer</h2>
  <ul>
    <li><i></i>Best performing Siege Protocol 2 servers currently on the market.</li>
    <li><i></i>GPXC control panel for easy server administration.</li>
    <li><i></i>Dedicated servers designed specifically for Siege Protocol 2.</li>
    <li><i></i>Built in SP2 web-admin panel.</li>
    <li><i></i>Unlimited Player Slots on all game servers.</li>
    <li><i></i>Personal and dedicated customer support.</li>
  </ul>
</section>

<div class="abs cta cta-order"><strong>Order New Services</strong><small>Go to order forms ➶</small></div>
<div class="abs cta cta-account"><strong>Manage Your Account</strong><small>Secure Client Login ●</small></div>

<aside class="abs tweets">
  <div class="tweets-head">Our Latest Tweets</div>
  <ul class="tweet-list">
    <li><i></i>Our new Las Vegas location is now online!<br><span>03:53:02 AM, October 31, 2012</span> from <span>web</span></li>
    <li><i></i>We are in the process of expanding to the west coast. Look for our new location (California) to come online before SP2's release!<br><span>05:38:01 AM July 21, 2012</span> from <span>web</span></li>
    <li><i></i>@SP2 Loving the new build! Our equipment is running loads better with the new improvements. Keep it up!<br><span>05:33:41 AM July 21, 2012</span> from <span>web</span><br><span>in reply to SP2</span></li>
    <li><i></i>Our new Virginia location is online! Check out our servers (http://kv7.co/Qx81pLz US EAST #1 - #5) and let us know how they perform.<br><span>@SP2 09:55:11 PM April 13, 2012</span> from <span>web</span></li>
  </ul>
</aside>

<footer class="abs footer"></footer>
<div class="abs fcol" style="left:108px"><h4>Our Services</h4><a>Game Servers</a><a>Dedicated Servers</a></div>
<div class="abs fcol" style="left:196px"><h4>Support</h4><a>Contact Us</a></div>
<div class="abs fcol" style="left:258px"><h4>Our Company</h4><a>About US</a><a>FAQs</a><a>Testimonials</a></div>
<div class="abs fcol" style="left:348px"><h4>Siege Protocol 2</h4><a>Buy Siege Protocol 2</a><a>Hidden Realm Studios</a><a>SP2HD</a></div>
<div class="abs badges"><i style="width:34px"></i><i style="width:88px"></i><i style="width:92px"></i></div>
<div class="abs social">Find us on: <i></i><i></i></div>
<div class="abs footer-rule"></div>
<div class="abs copyright">Copyright © 2013 KV7 Hosting</div>
</body>
</html>
```